Business cards for a recruitment company
Marrowby Associates
Modern
Helena Marrowby
Managing Director
PO Box 48213 Corvel Harbour Plaza Dubai United Arab Emirates
lena@marrowbyassociates-mail.test
marrowbyassociates-mail.test
The business card needs to have my name, designation etc in both English and Arabic. Therefore, both languages will appear on the front of the card. The final design will illustrate how two different translations will appear on the front of the card. **The logo must also appear on the front of the card.
The back of the card will be plain white with just the logo as attached in the AI file. Perhaps the logo could be indented.

```html
<!DOCTYPE html>
<html lang="en">
<head>
<meta charset="utf-8">
<title>Marrowby Associates — Stationery</title>
<link rel="stylesheet" href="https://fonts.googleapis.com/css2?family=Cinzel:wght@500&family=Open+Sans:wght@400;600&family=Noto+Kufi+Arabic:wght@400;600&display=swap">
<style>
  :root {
    --backdrop: #e8e8e9;
    --paper: #ffffff;
    --ink: #2b2629;
    --plum: #7d5f84;
    --text-grey: #7a7679;
    --band: #2e292d;
    --band-text: #e6e1e6;
    --rule: #d9d5da;
  }
  html, body {
    margin: 0;
    padding: 0;
    width: 1200px;
    height: 936px;
    overflow: hidden;
    background: var(--backdrop);
  }
  .canvas {
    position: relative;
    width: 1200px;
    height: 936px;
    font-family: "Open Sans", Arial, sans-serif;
    color: var(--text-grey);
  }
  .sheet {
    position: absolute;
    background: var(--paper);
    overflow: hidden;
    box-shadow: 0 1px 3px rgba(0,0,0,0.08);
  }

  /* Wordmark */
  .wordmark {
    display: flex;
    align-items: center;
    gap: 8px;
  }
  .wordmark__square {
    width: 14px;
    height: 14px;
    background: var(--plum);
    flex: none;
  }
  .wordmark__name {
    font-family: "Cinzel", "Times New Roman", serif;
    font-weight: 500;
    color: var(--ink);
    line-height: 1.05;
    font-size: 15px;
    letter-spacing: 0.06em;
    text-transform: uppercase;
    white-space: nowrap;
  }
  .wordmark__name span { display: block; }

  /* Footer band */
  .web-band {
    position: absolute;
    left: 0;
    right: 0;
    bottom: 0;
    background: var(--band);
    border-top: 3px solid var(--plum);
    color: var(--band-text);
    font-size: 7px;
    letter-spacing: 0.18em;
    display: flex;
    align-items: center;
    justify-content: center;
  }

  /* Letterhead */
  .letterhead { left: 185px; top: 68px; width: 386px; height: 554px; }
  .letterhead .wordmark { position: absolute; left: 22px; top: 30px; }
  .letterhead__contact {
    position: absolute;
    right: 26px;
    top: 28px;
    font-size: 5.5px;
    line-height: 1.6;
    font-style: normal;
  }
  .letterhead__body {
    position: absolute;
    left: 22px;
    top: 100px;
    width: 260px;
    font-size: 5.4px;
    line-height: 1.65;
  }
  .letterhead__body p { margin: 0 0 8px; }
  .letterhead__body strong { color: var(--ink); font-weight: 600; }
  .letterhead__signature {
    width: 34px;
    height: 14px;
    background: linear-gradient(90deg, #d3d0d3, #ecebec);
    margin: 4px 0 6px;
  }
  .letterhead__decoration {
    position: absolute;
    right: 10px;
    bottom: 26px;
    width: 150px;
    height: 170px;
    background: radial-gradient(ellipse at 50% 70%, #ebe9ec 0%, #f5f4f6 60%, var(--paper) 100%);
  }
  .letterhead .web-band { height: 18px; }

  /* Folder */
  .folder { left: 634px; top: 38px; width: 432px; height: 579px; }
  .folder .wordmark {
    position: absolute;
    left: 0;
    right: 0;
    top: 262px;
    justify-content: center;
  }
  .folder .wordmark__square { width: 24px; height: 24px; }
  .folder .wordmark__name { font-size: 24px; }
  .folder .web-band { height: 20px; }

  /* Business cards */
  .card { left: 46px; width: 152px; }
  .card--front { top: 655px; height: 96px; }
  .card--back { top: 781px; height: 102px; }
  .card .wordmark { gap: 4px; }
  .card .wordmark__square { width: 7px; height: 7px; }
  .card .wordmark__name { font-size: 8px; }
  .card--front .wordmark { position: absolute; left: 8px; top: 9px; }
  .card__details {
    position: absolute;
    top: 38px;
    font-size: 3.6px;
    line-height: 1.6;
    white-space: nowrap;
  }
  .card__details strong { color: var(--ink); font-weight: 600; font-size: 4.6px; }
  .card__details--en { left: 8px; width: 68px; }
  .card__details--ar {
    right: 8px;
    width: 60px;
    direction: rtl;
    text-align: right;
    font-family: "Noto Kufi Arabic", "Open Sans", sans-serif;
    font-size: 3.6px;
  }
  .card__divider {
    position: absolute;
    left: 79px;
    top: 38px;
    width: 1px;
    height: 46px;
    background: var(--rule);
  }
  .card__band {
    position: absolute;
    left: 0; right: 0; bottom: 0;
    height: 4px;
    background: var(--band);
    border-top: 1px solid var(--plum);
  }
  .card--back .wordmark {
    position: absolute;
    left: 0; right: 0; top: 44px;
    justify-content: center;
  }

  /* Compliment slip */
  .compliment { left: 264px; top: 672px; width: 360px; height: 211px; }
  .compliment .wordmark { position: absolute; left: 16px; top: 18px; }
  .compliment .wordmark__square { width: 10px; height: 10px; }
  .compliment .wordmark__name { font-size: 11px; }
  .compliment .web-band { height: 13px; font-size: 5.5px; }

  /* Envelope */
  .envelope { left: 738px; top: 672px; width: 419px; height: 211px; }
  .envelope__flap { position: absolute; left: 0; top: 0; }
</style>
</head>
<body>
<main class="canvas">

  <article class="sheet letterhead">
    <div class="wordmark">
      <div class="wordmark__square"></div>
      <div class="wordmark__name"><span>Marrowby</span><span>Associates</span></div>
    </div>
    <address class="letterhead__contact">
      PO Box 48213 Corvel Harbour Plaza<br>
      Dubai, UAE<br>
      T +971 4 555 0142<br>
      lena@marrowbyassociates-mail.test<br>
      marrowbyassociates-mail.test
    </address>
    <div class="letterhead__body">
      <p>May 12, 2025</p>
      <p>Dear Ms. Harlow,<br>Orrin Trading LLC, Dock Street</p>
      <p>Thank you for meeting with our team last week to discuss your hiring plans for the coming year. We have reviewed the roles you outlined and prepared a shortlist of candidates whose experience matches your needs in operations and finance.</p>
      <p>Each profile has been screened for skills, references and availability. We would welcome the chance to arrange interviews at a time that suits you and your managers.</p>
      <p>Please let us know if you have any questions about the terms of our agreement. We look forward to supporting your growth and building a lasting working relationship with your company.</p>
      <p>Best Regards,</p>
      <div class="letterhead__signature" role="img" aria-label="Handwritten signature"></div>
      <p><strong>Helena Marrowby</strong><br>Managing Director</p>
    </div>
    <div class="letterhead__decoration" role="img" aria-label="Faint decorative brand motif"></div>
    <footer class="web-band">www.marrowbyassociates-mail.test</footer>
  </article>

  <article class="sheet folder">
    <div class="wordmark">
      <div class="wordmark__square"></div>
      <div class="wordmark__name"><span>Marrowby</span><span>Associates</span></div>
    </div>
    <footer class="web-band">www.marrowbyassociates-mail.test</footer>
  </article>

  <article class="sheet card card--front">
    <div class="wordmark">
      <div class="wordmark__square"></div>
      <div class="wordmark__name"><span>Marrowby</span><span>Associates</span></div>
    </div>
    <div class="card__details card__details--en">
      <strong>Helena Marrowby</strong><br>
      Managing Director<br>
      PO Box 48213 Corvel Harbour Plaza<br>
      Dubai, United Arab Emirates<br>
      lena@marrowbyassociates-mail.test<br>
      marrowbyassociates-mail.test
    </div>
    <div class="card__divider"></div>
    <div class="card__details card__details--ar" lang="ar">
      <strong>هيلينا ماروبي</strong><br>
      المدير العام<br>
      ص.ب 48213 كورفل هاربر بلازا<br>
      دبي، الإمارات العربية المتحدة<br>
      <span dir="ltr">lena@marrowbyassociates-mail.test</span><br>
      <span dir="ltr">marrowbyassociates-mail.test</span>
    </div>
    <div class="card__band"></div>
  </article>

  <article class="sheet card card--back">
    <div class="wordmark">
      <div class="wordmark__square"></div>
      <div class="wordmark__name"><span>Marrowby</span><span>Associates</span></div>
    </div>
  </article>

  <article class="sheet compliment">
    <div class="wordmark">
      <div class="wordmark__square"></div>
      <div class="wordmark__name"><span>Marrowby</span><span>Associates</span></div>
    </div>
    <footer class="web-band">www.marrowbyassociates-mail.test</footer>
  </article>

  <article class="sheet envelope">
    <svg class="envelope__flap" width="419" height="211" viewBox="0 0 419 211" aria-hidden="true">
      <polygon points="0,0 419,0 419,22 209,90 0,22" fill="var(--band)"/>
      <polyline points="0,22 209,90 419,22" fill="none" stroke="var(--plum)" stroke-width="2"/>
    </svg>
  </article>

</main>
</body>
</html>
```